Brochure for cocktails machines!

Hello, Our company, Brewcraft, is manufacturing and distributing a cocktail machine called the Tavro Nine: https://www.pourvantix.com/en/cocktails-machine-automated-tavro-nine/ Our final customers are bars, hotels, restaurants , casino, catering companies ... The main idea for the product is to be able to make cocktails, easily (no training) and very quickly (15 sec). The product is used by the bartenders or the waiters and is usually placed behind the bar. For a bar owner, the main problem solved is hiring a good bartender. Our customers are not the huge bars or huge clubs making 1000 cocktails / day but that usually sells 5 to 100 cocktails / day. Of course they can do more! For this product, we need to design a new PDF brochure that we are interested in. We want something: - Easy to read - With beautiful pictures - Very clean and homogenous design. The final render must be on canva.com or anything else easily editable text by a non designer!). The format will be A4. You'll find in attachment: - the summary of what we want to show / demonstrate in this brochure (we are open to new ideas). - the prior materials that we were using (brochures, technical dataheets, sales proposals, pitchdecks ...) (some material is called StirKite which was the previous name of the company that was making a different cocktail machine!). - The logo of the company - Images: You'll find the HD renders of the different images of the product in the different colors: https://files.quenbarle.net/file/d/83kdqpwzmvTa20LxHrfuYebsNc5jO-Qw/view?usp= We are very open to other ideas. Do not hesitate to ask questions if you have!

Target Market(s)

Bars, hotels, restaurants, casinos, ...

Font styles to use
Sans Serif

Colors

Designer to choose colors to be used in the design.

Requirements
Must have
• In the summary doc

```html
<!DOCTYPE html>
<html lang="en">
<head>
<meta charset="UTF-8">
<title>Create and Manage Your Own Recipes</title>
<link href="https://fonts.googleapis.com/css2?family=Montserrat:wght@700;800&family=Open+Sans:wght@400&display=swap" rel="stylesheet">
<style>
  :root {
    --bg-light: #5b5756;
    --bg-mid: #3a3837;
    --bg-dark: #1b1b1b;
    --ink: #ffffff;
    --accent: #f2d77c;
    --line: #d9d9d9;
    --shot-bg: #f4f4f4;
    --shot-edge: #e2e2e2;
  }
  * { margin: 0; padding: 0; box-sizing: border-box; }
  html, body { width: 1200px; height: 848px; overflow: hidden; background: var(--bg-dark); }
  .page {
    position: relative;
    width: 1200px;
    height: 848px;
    overflow: hidden;
    background: radial-gradient(ellipse 75% 65% at 42% 18%, var(--bg-light) 0%, var(--bg-mid) 45%, var(--bg-dark) 100%);
    font-family: "Open Sans", Arial, sans-serif;
    color: var(--ink);
  }
  .headline {
    position: absolute;
    left: 113px;
    top: 44px;
    font-family: "Montserrat", Arial, sans-serif;
    font-weight: 700;
    font-size: 52px;
    line-height: 71px;
    letter-spacing: -0.3px;
    text-transform: uppercase;
    white-space: nowrap;
  }
  .intro {
    position: absolute;
    left: 761px;
    top: 89px;
    font-family: "Montserrat", Arial, sans-serif;
    font-weight: 700;
    font-size: 24px;
    line-height: 35px;
    letter-spacing: 2.5px;
    color: var(--accent);
    text-transform: uppercase;
    white-space: nowrap;
  }
  .screen {
    position: absolute;
    background: linear-gradient(180deg, #ffffff 0%, var(--shot-bg) 100%);
    border: 1px solid var(--shot-edge);
  }
  .screen--editor { left: 410px; top: 204px; width: 323px; height: 202px; }
  .screen--drinks { left: 410px; top: 435px; width: 323px; height: 240px; }
  .screen--dashboard { left: 763px; top: 435px; width: 342px; height: 240px; }
  .callout {
    position: absolute;
    font-size: 15.5px;
    line-height: 22.5px;
    white-space: nowrap;
  }
  .callout--editing { left: 101px; top: 297px; }
  .callout--custom { left: 95px; top: 492px; }
  .callout--updates { left: 134px; top: 696px; }
  .callout--stats { left: 601px; top: 696px; }
  .leaders { position: absolute; left: 0; top: 0; }
</style>
</head>
<body>
<main class="page">
  <h1 class="headline">Create and manage<br>your own recipes</h1>

  <p class="intro">Using the<br>built-in<br>backoffice<br>software,<br>you can<br>customize the<br>menu to fit<br>your unique<br>needs.</p>

  <div class="screen screen--editor" role="img" aria-label="Screenshot of the Backoffice cocktail recipe editor showing a Tequila Sunrise recipe and its ingredient steps"></div>
  <div class="screen screen--drinks" role="img" aria-label="Screenshot of the Backoffice drink list with custom variations of Caipirinha, Mojito, Margarita, Pina Colada, Caipiroska and Sex on the Beach"></div>
  <div class="screen screen--dashboard" role="img" aria-label="Screenshot of the Backoffice dashboard with sales totals, cocktails made per day chart and favourite recipes donut chart"></div>

  <svg class="leaders" width="1200" height="848" viewBox="0 0 1200 848" aria-hidden="true">
    <g fill="none" stroke="var(--line)" stroke-width="1">
      <line x1="87" y1="290" x2="410" y2="290"/>
      <rect x="81" y="287" width="6" height="6"/>
      <line x1="87" y1="481" x2="410" y2="481"/>
      <rect x="81" y="478" width="6" height="6"/>
      <line x1="566" y1="675" x2="566" y2="786"/>
      <rect x="563" y="786" width="6" height="6"/>
      <line x1="1042" y1="675" x2="1042" y2="790"/>
      <rect x="1039" y="790" width="6" height="6"/>
    </g>
  </svg>

  <p class="callout callout--editing">All recipes are editable and can be<br>deleted with our user friendly<br>Backoffice software that can be easily<br>accessed online from anywhere, no<br>installation necessary.</p>

  <p class="callout callout--custom">Backoffice software allows&nbsp; you to add<br>your own custom drinks, so you can<br>serve your customers with unique,<br>signature, and well made cocktails<br>each and everytime.</p>

  <p class="callout callout--updates">For your convenience, Backoffice will engage in<br>automatic software updates when connected to<br>internet, which will include access to new recipes as<br>our bartenders create them and share them with you!</p>

  <p class="callout callout--stats">Backoffice also provides you with statistics, such as<br>which drinks are most popular, how many drinks you<br>have sold, and what products are in high demand, so<br>that you can know your customers better.</p>
</main>
</body>
</html>
```